I'm looking for strong image and design for the first book in a series titled "Theodore Pellbrook On A Voyage Through Our Convictions" subtitle "Taking Hold of Living"; although it's about beliefs, I'm not look for an ethereal feel as the first book is about how our beliefs impact our actions and expectations. I'm a published philosopher and keen on branding my name for professional purposes hence the use of my name :) The book will initially be an e-book but I will follow up with a paperback soon afterwards. My website http://theodorepellbrook-example.com/ may provide some help on me and my projects. Thanks, Theo

Target Market(s)

Graduates and corporate folk who tend to lose their way in the systems.

Logo Text

Theodore Pellbrook on Convictions

Font styles to use
Sans Serif

Colors

Designer to choose colors to be used in the design.

Requirements
Must have
• Needless to say, but impact.
Nice to have
• Strong colours
Should not have
• Religious imagery; the book is philosophical and leans into living in this world.

```html
<!DOCTYPE html>
<html lang="en">
<head>
<meta charset="utf-8">
<title>Theodore Pellbrook — A Voyage Through Our Convictions</title>
<link rel="stylesheet" href="https://fonts.googleapis.com/css2?family=Archivo:wght@400;800&display=swap">
<style>
  :root {
    --backdrop: #9cc4a0;
    --ink: #1c3a2c;
    --panel: #cfcd95;
    --band-light: #c9cc6a;
    --band-dark: #1f3b26;
    --sky-glow: #b5bf5e;
    --sky-mid: #5d7a36;
    --sky-deep: #1d3620;
  }
  html, body {
    margin: 0;
    padding: 0;
    width: 1200px;
    height: 1200px;
    overflow: hidden;
    background: var(--backdrop);
  }
  .canvas {
    position: relative;
    width: 1200px;
    height: 1200px;
  }
  .book-cover {
    position: absolute;
    left: 203px;
    top: 40px;
    width: 793px;
    height: 1120px;
    background: var(--panel);
    overflow: hidden;
    font-family: "Archivo", "Helvetica Neue", Arial, sans-serif;
    color: var(--ink);
  }
  .author-band {
    position: absolute;
    left: 0; top: 0;
    width: 100%;
    height: 93px;
    background: linear-gradient(90deg, var(--band-light) 0%, #b8bd55 40%, #4f6a2e 65%, var(--band-dark) 85%);
  }
  .author-name {
    position: absolute;
    left: 44px;
    top: 22px;
    margin: 0;
    font-size: 42px;
    font-weight: 400;
    letter-spacing: 0.5px;
    line-height: 1;
    text-transform: uppercase;
  }
  .title-panel {
    position: absolute;
    left: 0; top: 93px;
    width: 100%;
    height: 502px;
    background: linear-gradient(180deg, #d3d19b 0%, var(--panel) 100%);
  }
  .book-title {
    position: absolute;
    left: 44px;
    top: 220px;
    margin: 0;
    font-size: 80px;
    font-weight: 800;
    line-height: 115px;
    text-transform: uppercase;
    letter-spacing: 0.5px;
  }
  .book-title span { display: block; height: 115px; }
  .book-subtitle {
    position: absolute;
    left: 44px;
    top: 541px;
    margin: 0;
    font-size: 42px;
    font-weight: 400;
    line-height: 1;
    text-transform: uppercase;
    letter-spacing: 0.5px;
  }
  .cover-image {
    position: absolute;
    left: 0; top: 595px;
    width: 100%;
    height: 525px;
    background:
      radial-gradient(ellipse 45% 35% at 30% 22%, rgba(190,198,100,0.85), rgba(190,198,100,0) 100%),
      radial-gradient(ellipse 60% 20% at 60% 78%, rgba(170,185,80,0.8), rgba(170,185,80,0) 100%),
      radial-gradient(ellipse 40% 40% at 85% 20%, rgba(25,50,30,0.9), rgba(25,50,30,0) 100%),
      linear-gradient(180deg, var(--sky-mid) 0%, #6e8a3e 45%, var(--sky-mid) 75%, var(--sky-deep) 100%);
  }
</style>
</head>
<body>
  <div class="canvas">
    <article class="book-cover">
      <header class="author-band">
        <p class="author-name">Theodore Pellbrook</p>
      </header>
      <section class="title-panel"></section>
      <h1 class="book-title">
        <span>A Voyage</span>
        <span>Through Our</span>
        <span>Convictions</span>
      </h1>
      <p class="book-subtitle">Taking Hold of Living</p>
      <div class="cover-image" role="img" aria-label="Photograph of a hazy green night sky with faint stars over a dark horizon, a lone figure seen from behind in silhouette"></div>
    </article>
  </div>
</body>
</html>
```